Letterhead design for Dental Practice - Ashby Lane Dental Care

Letterhead for Private Dental Practice. To be used for all official correspondance and for printing treatment details on to be given to patients.

Target Market(s)

Private dental patients

Industry/Entity Type

Dental Clinic

Font styles to use
Other font styles liked:
• nexa-light

Colors
33a6d7
1c66ac
85abd2

Requirements
Must have
• info in the footer and header needs to be 3.5cm from upper/lower boader of paper, see photo in uploaded files
• info details:
• tel. 0115 947 3051
• email info@ashbylanedc.co.uk
• ashbylanedentalcare.co.uk
• 17b Ashby Lane West Bridgford Nottingham NG2 7QT
• nexa-light font as in uploaded logo files
Should not have
• No funny tooth pictures

```html
<!DOCTYPE html>
<html lang="en">
<head>
<meta charset="utf-8">
<title>Ashby Lane Dental Care – Letterhead</title>
<link rel="stylesheet" href="https://fonts.googleapis.com/css2?family=Lato:wght@300;400;700&display=swap">
<style>
  :root {
    --brand-blue: #1a94d0;
    --ink: #1b1b1b;
    --charcoal: #3a3a3a;
    --paper: #f4f4f4;
    --backdrop: #e4e4e4;
    --signature-tint: #dfe1ea;
  }
  * { box-sizing: border-box; margin: 0; padding: 0; }
  html, body {
    width: 1200px; height: 1079px; overflow: hidden;
    background: var(--backdrop);
    font-family: "Lato", Arial, sans-serif;
    color: var(--ink);
  }
  .letterhead {
    position: absolute; left: 229px; top: 15px;
    width: 741px; height: 1048px;
    background: var(--paper);
    box-shadow: 0 2px 8px rgba(0,0,0,0.12);
    overflow: hidden;
  }
  .brand {
    position: absolute; left: 67px; top: 62px;
    display: flex; align-items: center; gap: 12px;
  }
  .brand-dot {
    width: 34px; height: 34px; border-radius: 50%;
    background: var(--brand-blue);
  }
  .brand-name {
    font-weight: 300; font-size: 29px; color: var(--brand-blue);
    letter-spacing: 0.3px;
  }
  .contact {
    position: absolute; left: 482px; top: 57px;
    border-left: 1px solid var(--charcoal);
    padding-left: 8px; height: 44px;
  }
  .contact-item {
    display: flex; align-items: center; gap: 8px;
    font-size: 12px; line-height: 15px; height: 15px;
  }
  .contact-item svg { width: 12px; height: 12px; flex: none; }
  .letter-body {
    position: absolute; left: 69px; top: 332px; width: 597px;
  }
  .salutation { font-size: 16px; margin-bottom: 16px; }
  .letter-body p.para {
    font-size: 12.3px; line-height: 16px; text-align: justify;
    margin-bottom: 10px;
  }
  .sign-off { position: absolute; left: 69px; top: 702px; font-size: 12.5px; line-height: 14px; }
  .sign-off .company { font-weight: 700; }
  .signature {
    position: absolute; left: 67px; top: 732px; width: 152px; height: 66px;
    background: var(--signature-tint); border-radius: 4px;
  }
  .role { position: absolute; left: 114px; top: 779px; font-size: 12.5px; }
  .address {
    position: absolute; left: 67px; top: 1000px;
    display: flex; align-items: center; gap: 4px;
    font-weight: 700; font-size: 12px;
  }
  .address svg { width: 10px; height: 13px; }
  .footer-band { position: absolute; left: 0; bottom: 0; width: 100%; height: 12px; display: flex; }
  .footer-band .band-blue { background: var(--brand-blue); }
  .footer-band .band-dark { background: var(--charcoal); }
</style>
</head>
<body>
<main class="letterhead">
  <header>
    <div class="brand">
      <span class="brand-dot"></span>
      <span class="brand-name">Ashby Lane Dental Care</span>
    </div>
    <div class="contact">
      <div class="contact-item">
        <svg viewBox="0 0 12 12"><circle cx="6" cy="6" r="5.3" fill="none" stroke="var(--brand-blue)" stroke-width="1.2"/><path d="M4 3.3l1 1.4-.6.7c.4.9 1.1 1.6 2 2l.7-.6 1.4 1-.5 1c-2.5-.3-4.3-2.2-4.6-4.6z" fill="var(--brand-blue)"/></svg>
        <span>0115 947 3051</span>
      </div>
      <div class="contact-item">
        <svg viewBox="0 0 12 12"><rect x="0.5" y="2.5" width="11" height="7.5" fill="var(--brand-blue)"/><path d="M0.8 3l5.2 4 5.2-4" fill="none" stroke="var(--paper)" stroke-width="1"/></svg>
        <span>info@ashbylanedc.co.uk</span>
      </div>
      <div class="contact-item">
        <svg viewBox="0 0 12 12" fill="none" stroke="var(--brand-blue)" stroke-width="1"><circle cx="6" cy="6" r="5.2"/><ellipse cx="6" cy="6" rx="2.3" ry="5.2"/><path d="M0.8 6h10.4M1.6 3.4h8.8M1.6 8.6h8.8"/></svg>
        <span>ashbylanedentalcare.co.uk</span>
      </div>
    </div>
  </header>

  <section class="letter-body">
    <p class="salutation">Dear Sir</p>
    <p class="para">Lorem Ipsum is simply dummy text of the printing and typesetting industry. Lorem Ipsum has been the industry's standard dummy text ever since the 1500s, when an unknown printer took a galley of type and scrambled it to make a type specimen book. I It was popularised in the 1960s with the release of Typorin sheets containing Lorem Ipsum passages, and more recently with desktop publishing software like Corvel PageBuilder including versions of Lorem Ipsum.</p>
    <p class="para">It is a long established fact that a reader will be distracted by the readable content of a page when looking at its layout. The point of using Lorem Ipsum is that it has a more-or-less normal distribution of letters, as opposed to using 'Content here.</p>
    <p class="para">The point of using Lorem Ipsum is that it has a more-or-less normal distribution of letters, as opposed to using 'Content here, content here', making it look like readable English. page editors now use Lorem Ipsum as their default model text, and a search for 'lorem ipsum' will uncover many web sites still in their infancy. Various versions have evolved over the years.</p>
    <p class="para">Printing and typesetting industry. Lorem Ipsum has been the industry's standard dummy text ever since the 1500s, when an unknown printer took a galley of type and scrambled it to make a type specimen book. I It was popularised in the 1960s with the release of Typorin sheets containing Lorem Ipsum passages, and more recently with desktop publishing software like Corvel PageBuilder including versions of Lorem Ipsum.</p>
  </section>

  <div class="sign-off">
    <p>Sincerely</p>
    <p class="company">Ashby Lane Dental Care</p>
  </div>
  <div class="signature" role="img" aria-label="Handwritten signature of the managing director"></div>
  <p class="role">Managing Director</p>

  <footer>
    <div class="address">
      <svg viewBox="0 0 10 13"><path d="M5 0.7a4.2 4.2 0 0 0-4.2 4.2C0.8 8 5 12.4 5 12.4s4.2-4.4 4.2-7.5A4.2 4.2 0 0 0 5 0.7z" fill="var(--brand-blue)"/><circle cx="5" cy="4.9" r="1.6" fill="var(--paper)"/></svg>
      <span>17b Ashby Lane West Bridgford Nottingham NG2 7QT</span>
    </div>
    <div class="footer-band">
      <span class="band-blue" style="width:67px"></span>
      <span class="band-dark" style="width:341px"></span>
      <span class="band-blue" style="flex:1"></span>
    </div>
  </footer>
</main>
</body>
</html>
```